Investment website design - investing in mutual funds

I need a design of a website (only homepage for now) dedicated to investment in mutual funds. Attached is a mock up with all the elements the homepage design should contain. The homepage should contain a logo in the upper left corner, the domain the website will run on is www.morvatelsko.cz , in the upper right corner there should be 2 buttons or links SIGN UP / SIGN IN. The bottom of the homepage should contain links to ABOUT US, FAQ, PRIVACY POLICY, CONTACT US.
Now the main elements on the homepage
1) Video that will explain how the investment works exactly, under this video we will have 3 illustrated icons like the ones attached (see 2nd attachement) that will show the potential investor what exactly they could get when investing with us (education for kids, happy life after they retire, regular monthly payment for the rest of their life).
2) On the right side next to the video we will have a calculator where a potential investor can play with the numbers, the investor can fill in the MONTHLY PAYMENT that he wants to invest regularly every month, the time frame of the investment - for how long he wants to invest. Once the potential investor selects those 2 variables we will calculate for him 2 options - either he can get a ONE TIME PAYOUT once he reaches his investment horizon or he can get a regular monthly payment for the rest of his life. Under the laculator there will be a button 'I want to invest ->'. The functionality of the calculator should be similar to the calculator that can be found here http://www.brovikbanka.cz/brovik-podilove-fondy/ and https://pelvaro.cz/.
The design should look similar to https://pelvaro.cz/ (font, colors, logo). We prefer white background in the area where we have the video and calculator. We also like the design of www.truvanex.com. Let me know if you have any questions.

```html
<!DOCTYPE html>
<html lang="en">
<head>
<meta charset="utf-8">
<title>morvatelsko.cz – Mutual Fund Investing</title>
<link href="https://fonts.googleapis.com/css2?family=Montserrat:wght@300;400;500&family=Courier+Prime:wght@400;700&display=swap" rel="stylesheet">
<style>
  :root {
    --teal: #41b2be;
    --coral: #e55a3a;
    --ink: #1c1c1c;
    --text: #3a3a3a;
    --muted: #8a8a8a;
    --line: #d4d4d4;
    --track: #e6e6e6;
    --footer: #f1f1f1;
    --white: #ffffff;
  }
  * { box-sizing: border-box; margin: 0; padding: 0; }
  html, body { width: 1200px; height: 771px; overflow: hidden; background: var(--white); }
  body { position: relative; font-family: "Montserrat", sans-serif; color: var(--text); }
  .abs { position: absolute; }

  .brand { left: 59px; top: 26px; font-size: 27px; font-weight: 500; color: var(--teal); letter-spacing: 0.2px; }
  .auth { top: 26px; height: 32px; width: 94px; color: var(--white); font-size: 14px; display: flex; align-items: center; justify-content: center; letter-spacing: 0.3px; }
  .auth-in { left: 947px; background: var(--teal); }
  .auth-up { left: 1046px; width: 94px; background: var(--coral); }

  .section-title { top: 132px; font-size: 31px; font-weight: 300; letter-spacing: 0.5px; }
  .video-title { left: 111px; color: var(--teal); }
  .calc-title { left: 685px; color: var(--ink); font-weight: 400; }

  .video { left: 111px; top: 188px; width: 500px; height: 280px; background: linear-gradient(100deg, #8a6a5a 0%, #d9d4cf 35%, #e8ebee 60%, #9aa6b4 100%); }
  .play { left: 326px; top: 292px; }

  .benefit-art { top: 503px; height: 92px; }
  .benefit-label { top: 605px; font-family: "Courier Prime", monospace; font-weight: 700; font-size: 14px; color: var(--text); white-space: nowrap; }

  .mono-label { font-family: "Courier Prime", monospace; font-weight: 700; font-size: 14px; color: var(--text); letter-spacing: 0.4px; }
  .amount-label { left: 686px; top: 184px; }
  .amount { left: 686px; top: 210px; width: 403px; height: 46px; border: 1px solid var(--line); font-size: 21px; font-weight: 300; color: var(--text); padding: 0 18px; display: flex; align-items: center; }
  .amount .placeholder { color: #c8c8c8; }
  .caret { display: inline-block; width: 1px; height: 22px; background: var(--ink); margin: 0 1px; }

  .length-label { left: 685px; top: 289px; }
  .length-value { left: 1011px; top: 286px; font-family: "Courier Prime", monospace; font-size: 18px; color: var(--teal); letter-spacing: 1px; }
  .length-value b { font-weight: 700; }
  .track { left: 686px; top: 325px; width: 403px; height: 6px; background: var(--track); border-radius: 3px; }
  .fill { left: 686px; top: 325px; width: 65px; height: 6px; background: var(--coral); border-radius: 3px; }
  .knob { left: 738px; top: 315px; width: 26px; height: 26px; border-radius: 50%; background: var(--teal); border: 2px solid var(--white); box-shadow: 0 1px 3px rgba(0,0,0,0.25); }
  .range-min, .range-max { top: 346px; font-size: 13px; color: var(--muted); }
  .range-min { left: 687px; }
  .range-max { left: 1033px; }

  .option { left: 686px; width: 403px; font-family: "Courier Prime", monospace; font-weight: 700; font-size: 20px; display: flex; align-items: center; justify-content: center; letter-spacing: 0.5px; }
  .option-once { top: 393px; height: 54px; border: 1px solid var(--teal); color: var(--teal); }
  .or { left: 686px; width: 403px; top: 458px; text-align: center; font-size: 13px; color: var(--muted); }
  .option-monthly { top: 488px; height: 55px; background: var(--teal); color: var(--white); }
  .cta { top: 563px; height: 55px; background: var(--coral); color: var(--white); letter-spacing: 1.5px; }
  .cta svg { margin-left: 24px; }

  .footer { left: 0; top: 727px; width: 1200px; height: 44px; background: var(--footer); display: flex; align-items: center; justify-content: center; font-size: 12px; color: var(--muted); letter-spacing: 0.3px; }
  .footer span.sep { margin: 0 12px; }
</style>
</head>
<body>
  <div class="abs brand">morvatelsko.cz</div>
  <div class="abs auth auth-in">SIGN IN</div>
  <div class="abs auth auth-up">SIGN UP</div>

  <h1 class="abs section-title video-title">Video About Our Product</h1>
  <div class="abs video" role="img" aria-label="Video still: smiling businesswoman in an office with colleagues in the background"></div>
  <svg class="abs play" width="72" height="72" viewBox="0 0 72 72" aria-hidden="true">
    <circle cx="36" cy="36" r="36" fill="#d62222"/>
    <path d="M28 22 L52 36 L28 50 Z" fill="#ffffff"/>
  </svg>

  <div class="abs benefit-art" style="left:151px;width:82px" role="img" aria-label="Illustration: stack of books with a graduation cap"></div>
  <div class="abs benefit-art" style="left:327px;width:86px;background:linear-gradient(#e55a3a33,#f0b03033)" role="img" aria-label="Illustration: cuckoo clock with coins"></div>
  <div class="abs benefit-art" style="left:505px;width:86px;background:linear-gradient(#41b2be22,#e55a3a22)" role="img" aria-label="Illustration: retired man playing golf"></div>
  <div class="abs benefit-art" style="left:151px;width:82px;background:linear-gradient(#41b2be33,#f0b03033)" aria-hidden="true"></div>
  <div class="abs benefit-label" style="left:111px">Education for Kids</div>
  <div class="abs benefit-label" style="left:306px">Passive Income</div>
  <div class="abs benefit-label" style="left:463px">Happy Retirement</div>

  <h2 class="abs section-title calc-title">Our Calculator</h2>
  <div class="abs mono-label amount-label">Regular Monthly Investment:</div>
  <div class="abs amount">$&nbsp;1<span class="caret"></span><span class="placeholder">00</span></div>

  <div class="abs mono-label length-label">ReguLength of Investment</div>
  <div class="abs length-value"><b>4</b> Years</div>
  <div class="abs track"></div>
  <div class="abs fill"></div>
  <div class="abs knob"></div>
  <div class="abs range-min">0</div>
  <div class="abs range-max">30 Years</div>

  <div class="abs option option-once">One Time Payout</div>
  <div class="abs or">Or</div>
  <div class="abs option option-monthly">Monthly Payment</div>
  <div class="abs option cta">I WANT TO INVEST
    <svg width="12" height="14" viewBox="0 0 12 14" aria-hidden="true"><path d="M0 0 L12 7 L0 14 Z" fill="#ffffff"/></svg>
  </div>

  <footer class="abs footer">
    <span>ABOUT US</span><span class="sep">|</span>
    <span>FAQ</span><span class="sep">|</span>
    <span>PRIVACY POLICY</span><span class="sep">|</span>
    <span>CONTACT US</span>
  </footer>
</body>
</html>
```